Standard logo business card

We are seeking a solid, somewhat understated professional design. We are a tech company. We like fonts similar to Aptifer Slab. Front side will be white with the contact information and a small version of our primary (Light background) logo.

(We have three people so we will have three names and titles)

Back side will hold our reverse logo on dark background along with the tagline:

"Intelligent annotation solutions for complex data"

Target Market(s)

Professionals, Tech

Industry/Entity Type

Business

Contact Information for Business Card

Name
Title

Phone
Email
City, State
Website

[We will email leading designer specific contact information)

Font styles to use
Serif

Requirements
Must have
• Colors are:
• Orange RGB 245,92,23
• Blue RGB 3,34,56
Nice to have
• We like a split with the Name and Title on the right and then contact details (below) on the left.

```html
<!DOCTYPE html>
<html lang="en">
<head>
<meta charset="utf-8">
<title>Norvanta Business Card</title>
<link rel="stylesheet" href="https://fonts.googleapis.com/css2?family=Michroma&display=swap">
<style>
  :root {
    --orange: rgb(245, 92, 23);
    --navy: #283445;
    --card-white: #f4f4f4;
    --card-shade: #e2e2e2;
    --backdrop: #b4bac1;
    --light-text: #ffffff;
  }
  html, body {
    margin: 0;
    padding: 0;
    width: 1200px;
    height: 887px;
    overflow: hidden;
    background: var(--backdrop);
    font-family: "Michroma", sans-serif;
  }
  .card {
    position: absolute;
    left: 100px;
    top: 158px;
    width: 1000px;
    height: 570px;
    background: radial-gradient(ellipse at 45% 40%, var(--card-white) 0%, var(--card-shade) 100%);
    overflow: hidden;
    box-shadow: 0 18px 40px rgba(40, 50, 60, 0.25);
  }
  .card-shapes {
    position: absolute;
    inset: 0;
  }
  .brand {
    position: absolute;
    left: 140px;
    top: 120px;
    display: flex;
    align-items: center;
    gap: 22px;
  }
  .brand-square {
    width: 46px;
    height: 46px;
    background: var(--orange);
  }
  .brand-name {
    font-family: "Michroma", sans-serif;
    font-size: 50px;
    color: var(--navy);
    letter-spacing: 1px;
    text-transform: lowercase;
  }
  .person {
    position: absolute;
    right: 60px;
    top: 268px;
    text-align: right;
    color: var(--navy);
  }
  .person-name {
    font-size: 21px;
    letter-spacing: 3px;
    text-transform: uppercase;
    margin: 0;
  }
  .person-title {
    font-size: 16px;
    letter-spacing: 3px;
    font-variant: small-caps;
    margin: 6px 0 0;
  }
  .contact {
    position: absolute;
    color: var(--light-text);
    font-size: 13px;
    letter-spacing: 2px;
    font-variant: small-caps;
    display: flex;
    align-items: center;
    gap: 14px;
    white-space: nowrap;
  }
  .contact-line-one { left: 190px; top: 440px; }
  .contact-line-two { left: 50px; top: 474px; }
  .contact-item {
    display: flex;
    align-items: center;
    gap: 7px;
  }
  .contact-icon {
    width: 16px;
    height: 16px;
    flex: none;
  }
</style>
</head>
<body>
  <main class="card">
    <svg class="card-shapes" viewBox="0 0 1000 570" width="1000" height="570" aria-hidden="true">
      <path d="M0 262 C 300 350, 480 372, 700 352 C 850 340, 950 385, 1000 418 L1000 430 C 950 398, 850 356, 700 368 C 480 388, 300 366, 0 278 Z" fill="var(--orange)"/>
      <path d="M0 284 C 300 372, 480 394, 700 374 C 850 362, 950 405, 1000 436 L1000 570 L0 570 Z" fill="var(--navy)"/>
    </svg>

    <div class="brand">
      <span class="brand-square"></span>
      <span class="brand-name">norvanta</span>
    </div>

    <div class="person">
      <p class="person-name">Marcus Whitfield</p>
      <p class="person-title">Managing Director</p>
    </div>

    <div class="contact contact-line-one">
      <span class="contact-item">
        <svg class="contact-icon" viewBox="0 0 16 16" aria-hidden="true"><circle cx="8" cy="8" r="8" fill="#fff"/><path d="M4 8.5 L8 4.5 L12 8.5 V12 H4 Z" fill="var(--navy)"/></svg>
        Suite # 410, Kent Bldg, NY 10482
      </span>
      <span class="contact-item">
        <svg class="contact-icon" viewBox="0 0 16 16" aria-hidden="true"><circle cx="8" cy="8" r="8" fill="#fff"/><circle cx="8" cy="8" r="4.5" fill="none" stroke="var(--navy)" stroke-width="1.2"/><path d="M3.5 8 H12.5 M8 3.5 V12.5" stroke="var(--navy)" stroke-width="1"/></svg>
        www.Norvantalabs.com
      </span>
    </div>

    <div class="contact contact-line-two">
      <span class="contact-item">
        <svg class="contact-icon" viewBox="0 0 16 16" aria-hidden="true"><circle cx="8" cy="8" r="8" fill="#fff"/><path d="M5 4 L7 4 L7.5 6.5 L6.5 7.5 C7 9 7.5 9.5 8.5 10 L9.5 9 L12 9.5 L12 11.5 C8 12 4.5 8.5 5 4 Z" fill="var(--navy)"/></svg>
        555-014-2290
      </span>
      <span class="contact-item">
        <svg class="contact-icon" viewBox="0 0 16 16" aria-hidden="true"><circle cx="8" cy="8" r="8" fill="#fff"/><rect x="5.5" y="3.5" width="5" height="9" rx="1" fill="var(--navy)"/></svg>
        555-017-6341
      </span>
      <span class="contact-item">
        <svg class="contact-icon" viewBox="0 0 16 16" aria-hidden="true"><circle cx="8" cy="8" r="8" fill="#fff"/><rect x="4" y="6" width="8" height="6" fill="var(--navy)"/><rect x="5.5" y="3.5" width="5" height="3" fill="var(--navy)"/></svg>
        555-019-4072
      </span>
      <span class="contact-item">
        <svg class="contact-icon" viewBox="0 0 16 16" aria-hidden="true"><circle cx="8" cy="8" r="8" fill="#fff"/><rect x="4" y="5" width="8" height="6" fill="var(--navy)"/><path d="M4 5 L8 8.5 L12 5" fill="none" stroke="#fff" stroke-width="0.8"/></svg>
        mail@Norvantalabs.com
      </span>
    </div>
  </main>
</body>
</html>
```